Bourbon whiskey bottle label

I need a bottle label for bourbon whiskey. Size 3" x 5" max. I want design in the label and not a rectangle/square label.

tandrolux = bourbon whiskey = tandro lux

I've attached an example of a label that I really like so maybe this will help inspire.

I'm open to any colors. I want it to stand out. I do like the thought of a white layered background with color design.

I would like it to at least have the following on it:
-tandrolux (logo attached) or just add it yourself
-Private Barrel Select
-Straight Bourbon Whiskey
-Proof (plus little box to write)
-ALC/VOL (plus little box to write)
-Plus an open area (no design) to write message.

bourbon whiskey drinkers and industry

whiskey bourbon, retail

• see project description
• see project description
• see project description

```html
<!DOCTYPE html>
<html lang="en">
<head>
<meta charset="utf-8">
<title>Tandrolux Bottle Label</title>
<link href="https://fonts.googleapis.com/css2?family=Cinzel:wght@400;700&display=swap" rel="stylesheet">
<style>
  :root {
    --page: #ece8e3;
    --label-navy: #211a48;
    --label-navy-deep: #17113a;
    --silver: #c9cbd3;
    --silver-mid: #8e90a4;
    --silver-light: #eef0f4;
    --whiskey-red: #c21e2b;
    --field-white: #ffffff;
    --field-text: #5a5a66;
  }
  html, body {
    margin: 0;
    padding: 0;
    width: 1200px;
    height: 800px;
    overflow: hidden;
    background: var(--page);
  }
  .canvas {
    position: relative;
    width: 1200px;
    height: 800px;
  }
  .label {
    position: absolute;
    left: 430px;
    top: 70px;
    width: 340px;
    height: 660px;
    font-family: "Cinzel", serif;
    color: var(--silver-light);
  }
  .label-shape {
    position: absolute;
    inset: 0;
  }
  .label-text {
    position: absolute;
    left: 0;
    width: 100%;
    text-align: center;
    margin: 0;
  }
  .barrel-select {
    top: 84px;
    font-size: 21px;
    line-height: 25px;
    font-weight: 400;
    letter-spacing: 0.5px;
  }
  .brand-name {
    top: 256px;
    font-size: 33px;
    line-height: 44px;
    font-weight: 700;
    color: var(--whiskey-red);
    letter-spacing: 1px;
  }
  .spirit-type {
    top: 320px;
    font-size: 17px;
    line-height: 21px;
    font-weight: 400;
  }
  .field-label {
    position: absolute;
    width: 76px;
    text-align: center;
    font-size: 10px;
    line-height: 12px;
    color: var(--field-text);
  }
  .field-label.alc { left: 72px; top: 434px; }
  .field-label.proof { left: 182px; top: 434px; }
</style>
</head>
<body>
<main class="canvas">
  <section class="label">
    <svg class="label-shape" viewBox="0 0 340 660" width="340" height="660" aria-hidden="true">
      <defs>
        <radialGradient id="seal-tone" cx="50%" cy="50%" r="50%">
          <stop offset="0%" stop-color="#211a48"/>
          <stop offset="74%" stop-color="#211a48"/>
          <stop offset="86%" stop-color="#6f7290"/>
          <stop offset="93%" stop-color="#b9bccb"/>
          <stop offset="100%" stop-color="#4a4b6a"/>
        </radialGradient>
        <linearGradient id="scroll-tone" x1="0" y1="0" x2="1" y2="0">
          <stop offset="0%" stop-color="#8e90a4" stop-opacity="0.6"/>
          <stop offset="50%" stop-color="#211a48" stop-opacity="0"/>
          <stop offset="100%" stop-color="#8e90a4" stop-opacity="0.6"/>
        </linearGradient>
      </defs>
      <path d="M30 70 Q20 70 20 50 L60 50 Q110 50 130 22 Q170 2 210 22 Q230 50 280 50 L320 50 Q320 70 310 70 Q335 330 310 590 Q320 590 320 610 L280 610 Q230 610 210 638 Q170 658 130 638 Q110 610 60 610 L20 610 Q20 590 30 590 Q5 330 30 70 Z"
            fill="var(--label-navy)" stroke="var(--silver)" stroke-width="3"/>
      <path d="M38 80 Q30 80 30 62 L62 62 Q116 62 136 34 Q170 16 204 34 Q224 62 278 62 L310 62 Q310 80 302 80 Q324 330 302 580 Q310 580 310 598 L278 598 Q224 598 204 626 Q170 644 136 626 Q116 598 62 598 L30 598 Q30 580 38 580 Q16 330 38 80 Z"
            fill="none" stroke="var(--silver)" stroke-width="1"/>
    </svg>
    <svg class="label-shape" viewBox="0 0 340 660" width="340" height="660" role="img" aria-label="Silver ornamental seal with beaded rings, laurel sprig, rosettes and scroll filigree">
      <circle cx="170" cy="300" r="144" fill="url(#seal-tone)"/>
      <circle cx="170" cy="300" r="144" fill="none" stroke="var(--silver)" stroke-width="2"/>
      <circle cx="170" cy="300" r="110" fill="none" stroke="var(--silver)" stroke-width="1.5"/>
      <rect x="50" y="470" width="240" height="44" fill="url(#scroll-tone)"/>
      <circle cx="58" cy="100" r="9" fill="var(--silver-mid)"/>
      <circle cx="282" cy="100" r="9" fill="var(--silver-mid)"/>
      <circle cx="58" cy="572" r="9" fill="var(--silver-mid)"/>
      <circle cx="282" cy="572" r="9" fill="var(--silver-mid)"/>
    </svg>
    <svg class="label-shape" viewBox="0 0 340 660" width="340" height="660" aria-hidden="true">
      <rect x="22" y="254" width="296" height="48" fill="var(--label-navy)"/>
      <line x1="30" y1="254" x2="310" y2="254" stroke="var(--silver)" stroke-width="1.5"/>
      <line x1="30" y1="302" x2="310" y2="302" stroke="var(--silver)" stroke-width="1.5"/>
      <g class="fields" fill="var(--field-white)" stroke="var(--silver)" stroke-width="3">
        <circle cx="110" cy="462" r="38"/>
        <circle cx="220" cy="462" r="38"/>
        <rect x="75" y="540" width="190" height="54" rx="10"/>
      </g>
    </svg>
    <p class="label-text barrel-select">Private Barrel<br>Select</p>
    <p class="label-text brand-name">TANDROLUX</p>
    <p class="label-text spirit-type">Straight Bourbon<br>Whiskey</p>
    <span class="field-label alc">ALC/VOL</span>
    <span class="field-label proof">Proof</span>
  </section>
</main>
</body>
</html>
```